Cool website to book tickets on a fleet of amazing jets

morph bookmarlowsky.com, an aspx live web page, and marlowsky.net into a landing page and website template. Add standard web pages including a press page, board member page, key personnel page.

Target Market(s)

People booking affordable private charter

Industry/Entity Type

Aviation

Coding

Coded - Design and coding required

Number of Pages Required

5+ page

Font styles to use
Other font styles liked:
• Possibly the aviation font

Requirements
Must have
• Allow bookmarlowsky.com to function, but can alter the design of those pages. A book now button that takes you to the bookmarlowsky function page. That can be built into a one url design.
Nice to have
• Repeat some of the colors of our jet livery.

```html
<!DOCTYPE html>
<html lang="en">
<head>
<meta charset="utf-8">
<title>Marlowsky – Private Jet Booking</title>
<link rel="stylesheet" href="https://fonts.googleapis.com/css2?family=Roboto+Slab:wght@400;500;700&family=Roboto:wght@400;500;700&display=swap">
<style>
:root{
  --blue:#0a5eab;
  --blue-dark:#074a89;
  --sky:#2f8fd8;
  --green:#8cc63f;
  --grey-bg:#f3f3f3;
  --text:#333;
  --muted:#555;
  --footer:#141414;
  --white:#fff;
}
*{margin:0;padding:0;box-sizing:border-box}
html,body{width:1200px;height:4153px;overflow:hidden}
body{position:relative;font-family:"Roboto Slab",serif;color:var(--text);background:var(--white)}
.abs{position:absolute}
.slab{font-family:"Roboto Slab",serif}
.sans{font-family:"Roboto",sans-serif}
.hl-green{color:var(--green)}
.hl-blue{color:var(--blue)}

/* top bar */
.topbar{left:0;top:0;width:1200px;height:31px;background:var(--blue);color:#fff;font-size:13px}
.topbar span{position:absolute;top:8px}
.topbar svg{position:absolute;top:8px}
.sq{position:absolute;top:8px;width:14px;height:14px;background:#fff;border-radius:2px}

/* header */
.header{left:0;top:31px;width:1200px;height:106px;background:#fff}
.brand{position:absolute;font-family:"Roboto Slab",serif;font-weight:700;color:var(--blue);letter-spacing:1px}
.brand-dot{display:inline-block;width:14px;height:14px;border-radius:50%;background:var(--sky);margin-right:8px;vertical-align:middle}
.nav a{position:absolute;top:45px;font-family:"Roboto",sans-serif;font-size:14px;font-weight:500;color:#222;text-decoration:none}
.nav a.active{color:var(--blue)}
.btn{position:absolute;display:flex;align-items:center;justify-content:center;color:#fff;text-decoration:none;font-family:"Roboto Slab",serif;text-transform:uppercase}
.btn-sky{background:var(--sky)}
.btn-green{background:var(--green)}
.btn-blue{background:var(--blue)}

/* hero */
.hero{left:0;top:137px;width:1200px;height:528px;background:linear-gradient(160deg,#5b8cb6 0%,#4a7ba8 45%,#6f9bc2 100%)}
.hero-welcome{left:0;width:1200px;top:120px;text-align:center;font-size:32px;font-weight:700;color:var(--green)}
.hero-title{left:0;width:1200px;top:165px;text-align:center;font-size:76px;font-weight:700;color:#fff;letter-spacing:2px}
.dots{left:554px;top:488px}
.dots i{display:inline-block;width:22px;height:7px;background:#fff;margin-right:13px}
.dots i:first-child{background:var(--green)}

/* booking */
.tab{position:absolute;top:665px;height:42px;display:flex;align-items:center;justify-content:center;color:#fff;font-weight:700;font-size:17px}
.booking{left:65px;top:713px;width:1069px;height:89px;background:var(--blue)}
.field{position:absolute;top:24px;height:42px;background:#fff;font-size:12px;padding:14px 13px;color:#222}

/* CEO */
.ceo{left:0;top:890px;width:1200px;height:449px;background:var(--grey-bg)}
.section-title{position:absolute;font-weight:700;font-size:44px;white-space:nowrap}
.body-text{position:absolute;font-size:13px;line-height:21px;color:var(--muted)}
.name-tag{position:absolute;background:var(--green);color:#fff;font-size:22px;display:flex;align-items:center;justify-content:center}

/* partner */
.partner{left:0;top:1427px;width:1200px;height:447px;background:var(--grey-bg)}
.point h3{font-weight:500;font-size:21px;color:var(--green)}
.point p{font-size:13px;color:var(--muted);margin-top:6px}

/* IP */
.ip{left:0;top:1963px;width:1200px;height:405px}
.ip-panel{left:544px;top:0;width:656px;height:405px;background:var(--blue);color:#fff;overflow:hidden}
.ip-title{left:25px;top:18px;font-size:38px;font-weight:700;white-space:nowrap}
.ip-list{position:absolute;left:55px;top:100px;width:560px;list-style:none}
.ip-list li{font-size:15px;font-weight:700;line-height:35px;position:relative;padding-left:0}
.ip-list li.lead::before{content:"";position:absolute;left:-29px;top:12px;width:11px;height:11px;border-radius:50%;background:var(--green)}
.ip-list li.sub{font-size:13px;padding-left:42px}
.ip-list li.sub svg{position:absolute;left:14px;top:12px}

/* features */
.feature{position:absolute;width:300px;text-align:center;color:var(--green);font-size:21px;line-height:36px}
.feature-icon{position:absolute;width:66px;height:66px;border-radius:50%;background:var(--sky)}

/* news */
.card{position:absolute;top:2787px;width:322px}
.card-img{width:322px;height:250px}
.card h4{margin:26px 0 0 8px;font-size:19px;font-weight:500}
.meta{margin:12px 0 0 8px;font-size:13px;color:#222;display:flex;align-items:center;gap:5px}
.meta i{display:inline-block;width:11px;height:11px;border-radius:50%;background:var(--green)}
.card p{margin:30px 0 0 8px;width:300px;font-size:13px;line-height:23px;color:var(--muted)}
.card .btn{position:relative;margin:28px 0 0 8px;width:121px;height:44px;font-size:14px}

/* partners */
.logo-word{position:absolute;top:3552px;font-family:"Roboto Slab",serif;font-weight:500;font-size:36px;color:var(--sky);display:flex;align-items:center;white-space:nowrap}
.logo-word .mark{width:40px;height:40px;border-radius:50%;background:var(--sky);margin-right:12px;flex:none}
.logo-word.dark{color:var(--blue)}
.logo-word.dark .mark{background:var(--blue)}
.logo-box{position:absolute;left:576px;top:3541px;width:80px;height:80px;background:#000;color:#fff;font-family:"Roboto Slab",serif;font-size:22px;display:flex;align-items:center;justify-content:center}

/* footer */
.footer{left:0;top:3747px;width:1200px;height:406px;background:var(--footer);color:#fff}
.f-head{position:absolute;top:71px;font-family:"Roboto",sans-serif;font-weight:500;font-size:14px}
.f-link{position:absolute;font-family:"Roboto",sans-serif;font-size:13px}
.f-input{position:absolute;left:824px;top:92px;width:228px;height:48px;background:#fff;color:#222;font-size:12px;padding:17px 14px}
.f-search{position:absolute;left:1052px;top:92px;width:61px;height:48px;background:var(--sky)}
.f-social{position:absolute;top:188px;width:28px;height:28px;background:#fff;border-radius:3px}
.f-rule{position:absolute;left:89px;top:355px;width:1024px;height:1px;background:#555}
</style>
</head>
<body>

<!-- top bar -->
<div class="abs topbar">
  <svg style="left:65px" width="13" height="13" viewBox="0 0 24 24"><path fill="#fff" d="M6.6 10.8c1.4 2.8 3.8 5.1 6.6 6.6l2.2-2.2c.3-.3.7-.4 1-.2 1.1.4 2.3.6 3.6.6.6 0 1 .4 1 1V20c0 .6-.4 1-1 1C10.6 21 3 13.4 3 4c0-.6.4-1 1-1h3.5c.6 0 1 .4 1 1 0 1.3.2 2.5.6 3.6.1.3 0 .7-.2 1z"/></svg>
  <span style="left:97px">+1 555 0142</span>
  <svg style="left:190px" width="14" height="12" viewBox="0 0 24 20"><path fill="#fff" d="M2 0h20c1.1 0 2 .9 2 2v16c0 1.1-.9 2-2 2H2c-1.1 0-2-.9-2-2V2C0 .9.9 0 2 0zm10 11 10-7V2L12 9 2 2v2z"/></svg>
  <span style="left:218px">info@marlowsky.com</span>
  <i class="sq" style="left:874px"></i><i class="sq" style="left:904px"></i><i class="sq" style="left:930px"></i>
  <svg style="left:982px" width="13" height="13" viewBox="0 0 24 24"><circle cx="16" cy="8" r="6" fill="#fff"/><path d="M12 12 3 21" stroke="#fff" stroke-width="3"/></svg>
  <span style="left:1010px">Login</span>
  <svg style="left:1086px" width="14" height="14" viewBox="0 0 24 24"><circle cx="12" cy="12" r="10" fill="none" stroke="#fff" stroke-width="3"/><path d="M2 12h20M12 2v20" stroke="#fff" stroke-width="2"/></svg>
  <span style="left:1114px">EN</span>
</div>

<!-- header -->
<header class="abs header">
  <div class="brand" style="left:65px;top:34px;font-size:30px"><span class="brand-dot"></span>MARLOWSKY</div>
  <nav class="nav">
    <a class="active" style="left:567px">HOME</a>
    <a style="left:646px">ABOUT US</a>
    <a style="left:752px">NEWS</a>
    <a style="left:830px">CONTACT US</a>
  </nav>
  <a class="btn btn-sky" style="left:986px;top:31px;width:148px;height:45px;font-size:16px">Book Now</a>
</header>

<!-- hero -->
<section class="abs hero" role="img" aria-label="Private single-engine jet with blue livery parked on a reflective apron, blue-tinted photo">
  <div class="abs hero-welcome slab">WELCOME FOR</div>
  <div class="abs hero-title slab">MARLOWSKY</div>
  <div class="abs dots"><i></i><i></i><i></i></div>
</section>

<!-- booking -->
<div class="tab" style="left:203px;width:262px;background:var(--blue)">One-way</div>
<div class="tab" style="left:469px;width:262px;background:var(--green)">Round-trip</div>
<div class="tab" style="left:735px;width:262px;background:var(--green)">Multi-Leg</div>
<form class="abs booking">
  <div class="field" style="left:48px;width:172px">DEPARTURE</div>
  <div class="field" style="left:232px;width:172px">ARRIVAL</div>
  <div class="field" style="left:448px;width:173px">PASSENGER</div>
  <div class="field" style="left:633px;width:173px">DATE &amp; TIME</div>
  <a class="btn btn-green" style="left:850px;top:24px;width:174px;height:42px;font-size:15px">Book Now</a>
</form>

<!-- CEO -->
<section class="abs ceo">
  <svg class="abs" style="left:0;top:0" width="322" height="449" role="img" aria-label="Portrait of the CEO wearing a headset in a cockpit">
    <defs><linearGradient id="ceoG" x1="0" y1="0" x2="1" y2="1"><stop offset="0" stop-color="#c9a57c"/><stop offset=".5" stop-color="#7b6350"/><stop offset="1" stop-color="#3f3a36"/></linearGradient></defs>
    <polygon points="0,0 142,0 322,72 150,449 0,449" fill="url(#ceoG)"/>
  </svg>
  <div class="name-tag slab" style="left:173px;top:323px;width:221px;height:42px">DANIEL OSTROW</div>
  <h2 class="section-title" style="left:413px;top:48px"><span class="hl-green">FROM THE</span> <span class="hl-blue">CEO</span></h2>
  <p class="body-text" style="left:455px;top:127px;width:560px">Marlowsky is the culmination of a decades long journey to increase the effective speed door to door, reduce carbon and noise footprint and open private aviation to more people – unlocking the fourth wave of high speed travel. We will introduce disruptive personal mobility to ensure the safety of the family. During past several months, COVID-19 has significantly increased the demand for our services.</p>
  <p class="body-text" style="left:455px;top:274px;width:560px">Thank you for taking the time today to learn about this journey.</p>
</section>

<!-- partner -->
<section class="abs partner">
  <h2 class="section-title" style="left:65px;top:68px"><span class="hl-green">AS A HARBORLINE</span> <span class="hl-blue">PARTNER</span></h2>
  <div class="abs point" style="left:65px;top:170px"><h3>Routinely winning the Bid</h3><p>Cheaper and In position – lowest cost to reposition</p></div>
  <div class="abs point" style="left:437px;top:170px"><h3>Enables B2B vs B2C Model</h3><p>Access to substantial demand (unmet or lower price)</p></div>
  <div class="abs point" style="left:65px;top:260px"><h3>Minimal Marketing Costs</h3><p>Electronically booked - $0 Marketing Cost</p></div>
  <div class="abs point" style="left:437px;top:260px"><h3>Exclusive for 7 Years</h3><p>For Single Engine Jet Category</p></div>
  <svg class="abs" style="left:861px;top:0" width="339" height="447" role="img" aria-label="Pilot in flight helmet and oxygen mask giving a thumbs up">
    <defs><linearGradient id="pilG" x1="0" y1="0" x2="1" y2="1"><stop offset="0" stop-color="#6d7780"/><stop offset=".5" stop-color="#c9b7a4"/><stop offset="1" stop-color="#3d4248"/></linearGradient></defs>
    <polygon points="0,80 230,0 339,0 339,447 0,447" fill="url(#pilG)"/>
  </svg>
</section>

<!-- IP advantage -->
<section class="abs ip">
  <div class="abs" style="left:0;top:0;width:544px;height:405px;background:linear-gradient(170deg,#dfe6ec 0%,#8fa8bd 45%,#3d6a8e 100%)" role="img" aria-label="Three private jets in formation flight over a coastline"></div>
  <div class="abs ip-panel">
    <h2 class="abs slab ip-title">MARLOWSKY’S IP ADVANTAGE</h2>
    <ul class="ip-list">
      <li class="lead">US Patent Application for Novel Method of Accelerating Dynamic Availability and Pricing in Fleets</li>
      <li class="sub"><svg width="14" height="11" viewBox="0 0 14 11"><path d="M1 5.5 5 9.5 13 1.5" stroke="#fff" stroke-width="2.5" fill="none"/></svg>Related IP Processes and Software</li>
      <li class="sub"><svg width="14" height="11" viewBox="0 0 14 11"><path d="M1 5.5 5 9.5 13 1.5" stroke="#fff" stroke-width="2.5" fill="none"/></svg>Plan to file internationally preserving US filing date</li>
      <li class="lead">Developer/owner of software interfaces with Harborline and other system providers</li>
      <li class="lead">US Trademark/Service Mark filings on Marlowsky and our stylized logo</li>
      <li class="sub"><svg width="14" height="11" viewBox="0 0 14 11"><path d="M1 5.5 5 9.5 13 1.5" stroke="#fff" stroke-width="2.5" fill="none"/></svg>Plan to file internationally preserving US filing date</li>
    </ul>
  </div>
</section>

<!-- features -->
<div class="feature-icon" style="left:206px;top:2464px" role="img" aria-label="Strength icon"></div>
<div class="feature-icon" style="left:559px;top:2464px" role="img" aria-label="Quiet noise icon"></div>
<div class="feature-icon" style="left:920px;top:2464px" role="img" aria-label="Globe icon"></div>
<div class="feature" style="left:89px;top:2563px">TON CO2 Saved Per<br>Flight Segment</div>
<div class="feature" style="left:442px;top:2563px">Radical Noise<br>Reduction</div>
<div class="feature" style="left:803px;top:2563px">Lowest C02 Footprint</div>

<!-- news -->
<h2 class="section-title" style="left:94px;top:2704px"><span class="hl-green">LATEST</span> <span class="hl-blue">NEWS</span></h2>
<a class="btn btn-green" style="left:961px;top:2715px;width:144px;height:45px;font-size:15px">View All</a>

<article class="card" style="left:94px">
  <div class="card-img" role="img" aria-label="Private jet with open canopy parked on a runway" style="background:linear-gradient(180deg,#c7ccd1 0%,#8a97a3 55%,#4b4f53 100%)"></div>
  <h4 class="hl-green">POST TITLE GOES HERE</h4>
  <div class="meta"><i></i>Lifestyle, Luxury <i></i>Admin <i></i>2 Comments</div>
  <p>Lorem ipsum dolor sit amet, consectetur adipiscing elit. Proin nibh augue, suscipit a, scelerisque sed, lacinia in, mi. Cras vel lorem. Donec venenatis, turpis vel hendrerit interdum, dui ligula ultricies purus.</p>
  <a class="btn btn-green">Read More</a>
</article>
<article class="card" style="left:439px">
  <div class="card-img" role="img" aria-label="Three jets flying in formation above the coast" style="background:linear-gradient(170deg,#d7dde3 0%,#8ea6ba 50%,#46708f 100%)"></div>
  <h4 class="hl-blue">POST TITLE GOES HERE</h4>
  <div class="meta"><i></i>Lifestyle, Luxury <i></i>Admin <i></i>2 Comments</div>
  <p>Lorem ipsum dolor sit amet, consectetur adipiscing elit. Proin nibh augue, suscipit a, scelerisque sed, lacinia in, mi. Cras vel lorem. Donec venenatis, turpis vel hendrerit interdum, dui ligula ultricies purus.</p>
  <a class="btn btn-blue">Read More</a>
</article>
<article class="card" style="left:784px">
  <div class="card-img" role="img" aria-label="Private jet with open canopy parked on a runway" style="background:linear-gradient(180deg,#c7ccd1 0%,#8a97a3 55%,#4b4f53 100%)"></div>
  <h4 class="hl-green">POST TITLE GOES HERE</h4>
  <div class="meta"><i></i>Lifestyle, Luxury <i></i>Admin <i></i>2 Comments</div>
  <p>Lorem ipsum dolor sit amet, consectetur adipiscing elit. Proin nibh augue, suscipit a, scelerisque sed, lacinia in, mi. Cras vel lorem. Donec venenatis, turpis vel hendrerit interdum, dui ligula ultricies purus.</p>
  <a class="btn btn-green">Read More</a>
</article>

<!-- partners -->
<h2 class="section-title" style="left:0;width:1200px;top:3422px;text-align:center"><span class="hl-green">OUR</span> <span class="hl-blue">PARTNERS</span></h2>
<div class="logo-word" style="left:-20px"><span class="mark"></span>HARBORLINE</div>
<div class="logo-word dark" style="left:296px"><span class="mark"></span>Tripwise</div>
<div class="logo-box">Rydeo</div>
<div class="logo-word" style="left:702px"><span class="mark"></span>HARBORLINE</div>
<div class="logo-word dark" style="left:1023px"><span class="mark"></span>Tripwise</div>

<!-- footer -->
<footer class="abs footer">
  <div class="brand" style="left:89px;top:64px;font-size:36px;color:#fff">MARLOWSKY</div>
  <div class="abs sans" style="left:89px;top:169px;font-size:15px;font-weight:500">About Us</div>
  <p class="abs" style="left:89px;top:207px;width:290px;font-size:13px;line-height:23px">Lorem ipsum dolor sit amet, consectetur adipiscing elit. Proin nibh augue, suscipit a, scelerisque sed, lacinia in, mi. Cras vel lorem. Etiam pellentesque aliquet tellus. Phasellus pharetra nulla ac diam.</p>

  <div class="f-head" style="left:450px">LINKS</div>
  <div class="f-link" style="left:450px;top:114px">HOME</div>
  <div class="f-link" style="left:450px;top:156px">ABOUT US</div>
  <div class="f-link" style="left:450px;top:198px">NEWS</div>
  <div class="f-link" style="left:450px;top:240px">CONTACT US</div>

  <div class="f-head" style="left:613px">CONTACT US</div>
  <svg class="abs" style="left:613px;top:115px" width="13" height="13" viewBox="0 0 24 24"><path fill="#fff" d="M6.6 10.8c1.4 2.8 3.8 5.1 6.6 6.6l2.2-2.2c.3-.3.7-.4 1-.2 1.1.4 2.3.6 3.6.6.6 0 1 .4 1 1V20c0 .6-.4 1-1 1C10.6 21 3 13.4 3 4c0-.6.4-1 1-1h3.5c.6 0 1 .4 1 1 0 1.3.2 2.5.6 3.6.1.3 0 .7-.2 1z"/></svg>
  <div class="f-link" style="left:641px;top:114px">+1 555 0142</div>
  <svg class="abs" style="left:613px;top:158px" width="13" height="11" viewBox="0 0 24 20"><path fill="#fff" d="M2 0h20c1.1 0 2 .9 2 2v16c0 1.1-.9 2-2 2H2c-1.1 0-2-.9-2-2V2C0 .9.9 0 2 0zm10 11 10-7V2L12 9 2 2v2z"/></svg>
  <div class="f-link" style="left:641px;top:156px">info@marlowsky.com</div>

  <div class="f-head" style="left:824px">LATEST NEWS</div>
  <div class="f-input">ENTER YOUR EMAIL</div>
  <div class="f-search"><svg style="position:absolute;left:19px;top:13px" width="23" height="23" viewBox="0 0 24 24"><circle cx="10" cy="10" r="7" fill="none" stroke="#fff" stroke-width="3"/><path d="M15 15 22 22" stroke="#fff" stroke-width="3"/></svg></div>
  <i class="f-social" style="left:898px"></i>
  <i class="f-social" style="left:943px"></i>
  <i class="f-social" style="left:988px"></i>
  <i class="f-social" style="left:1033px"></i>

  <div class="f-rule"></div>
  <div class="abs" style="left:0;width:1200px;top:373px;text-align:center;font-size:14px">© 2020 All right reserved by MARLOWSKY</div>
</footer>

</body>
</html>
```